Church Website with Home Page and Member Sermon Library

I am in need of an updated design for our church website. This will include 4 pages (outlined below). We are a conservative, evangelical, Christian church. The site should be modern and clean, while still reflecting our conservative values. I already have a logo for our church, and I want the site to incorporate the logo, and match the logo/branding. Stock photos are allowed if needed, but I have uploaded some images of our church and would prefer those images to be used if possible. Any stock photos used should not include any people in the photos (scenery, nature, buildings, animals, etc. are fine).

The site will need 4 pages: Home, Support Us (Donate), Login, and Recording Library.

Page 1: Home
The home page should include the following sections:

- Navigation: Should include links to each section of the home page plus a "listen live" link which will take the user to a live-streaming site and a "support us" link which will take the user to a support/donate page.

- Announcements: Can be either a banner or some other design, but there needs to be some way for us to post announcements for visitors to see. I'm open for creative ideas in this section, but would like it not to take up a lot of room on the page.

- About Us: Should include address, service times (see attached document), and information about the church.

- Pastor Bio: A section that introduces our pastor and gives a short bio about our pastor. Would like this section to include a picture of our pastor. Somewhere in this section I would like to include this Bible reference: "And I will give you pastors according to mine heart, which shall feed you with knowledge and understanding. Jer 3:15 KJV"

- Articles of Faith (What We Believe): This should include several sub-sections each with a heading, body, and possibly 1 or more scripture references. I have attached a document to the brief that includes our articles of faith. Feel free to be creative with this section in how you lay these out and format them.

- Support Us: A small section that explains what kind of support someone can give and a link to a donation page. The link can say something like "Support Us" or "Donate Now".

- Contact form: A contact form that allows the visitor to send us a message. The contact form should ask for name, email, phone, and message.

- Footer: A footer that will be displayed on all pages of the site. This should include at a minimum a link to the home page (or a link to each individual section in the home page if you prefer), a link to "listen live", a link to "support us", a link to "contact us" (or you can put the contact form directly in the footer if you prefer), the address, and a "member login" link.

Page 2: Support Us
The donation page should include a form the visitor can fill out to make a donation. We will embed a third party form later. For this design, please just mock out the design with a basic form asking for name, phone, and email.

Page 3: Login
The recording library (detailed below) will require members to login with a shared numeric code before accessing the page. We need a design for a login screen. The screen should include navigation/footer just like all other pages, but the body of the login page will consist only of a form that asks the user to enter the access code and then a "login" button.

Page 4: Recording Library

The library page is a member-only page that will require a shared, numeric pass code to access. On this page, members will be able to access a filterable list of past sermons. The page by default should display most recent sermons, but should also include a search form that allows the member to filter the sermon list to find a particular sermon. The search form should allow the user to select a filter type (e.g. Speaker name, date, event, etc.) and type in a value to search. They should be able to add multiple filters and remove filters that have been added. Each sermon that is displayed in the result list should include basic information such as title, date, speaker, tags, etc. along with a download icon, and an embedded audio player where they can click a play button to stream it on-demand. Each sermon should also have clickable tags associated with it that can be used to find related sermons.
Updates

Need extra days to review

I have uploaded several images of our church. Feel free to incorporate these into your design if possible.

Target Market(s)

Church Members

Industry/Entity Type

Religion

Number of Pages Required

4 page

Font styles to use
Sans Serif

Colors

Designer to choose colors to be used in the design.

Requirements
Must have
• Must incorporate the logo (attached)
Nice to have
• Would like the design to incorporate pictures of our church (attached) instead of stock photos if possible.
Should not have
• Please avoid an overly cluttered design. Stock photos used should not include any people in the photos.

```html
<!DOCTYPE html>
<html lang="en">
<head>
<meta charset="utf-8">
<title>Grace Covenant Church — Home</title>
<link href="https://fonts.googleapis.com/css2?family=Cinzel:wght@400;500;700&family=Lato:ital,wght@0,400;0,700;0,900;1,700&display=swap" rel="stylesheet">
<style>
:root{
  --teal:#00b4d4;
  --green:#7fa866;
  --green-dark:#4e7232;
  --green-deep:#3f5f26;
  --ink:#333;
  --body:#555;
  --white:#fff;
  --sky:#d8d9db;
}
*{box-sizing:border-box;margin:0;padding:0}
html,body{width:1200px;height:5111px;overflow:hidden;background:var(--white)}
body{font-family:'Lato',sans-serif;color:var(--body);position:relative}
.abs{position:absolute}
.serif{font-family:'Cinzel',serif}
.section{position:absolute;left:0;width:1200px;overflow:hidden}
.pill{position:absolute;display:flex;align-items:center;justify-content:center;border-radius:30px;font-family:'Cinzel',serif;color:var(--white);font-size:15px;letter-spacing:.5px;text-decoration:none}

/* hero */
.hero{top:0;height:774px;background:linear-gradient(180deg,#e6e6e6 0%,#cfd0d2 38%,#b89a7a 62%,#8c6a4e 82%,#6f6a52 100%)}
.hours{left:48px;top:46px;color:#333}
.hours h3{font-family:'Cinzel',serif;font-weight:400;font-size:20px;display:flex;align-items:center;gap:10px;margin-bottom:10px}
.hours table{border-collapse:collapse;font-size:13px}
.hours td{padding:3px 0;height:25px}
.hours td.c{padding:0 22px 0 42px}
.brand{left:400px;top:110px;width:400px;text-align:center;font-family:'Cinzel',serif;color:var(--green);font-size:44px;line-height:1.1;font-weight:400}
.top-btn{top:52px;height:40px;font-size:15px}
.nav{right:52px;top:122px;text-align:right;font-family:'Cinzel',serif;font-size:15px;line-height:27px;color:#222}
.nav a{display:block;color:inherit;text-decoration:none}
.nav a.active{color:var(--teal)}
.headline{left:0;width:1200px;top:300px;text-align:center;font-weight:900;font-size:50px;line-height:58px;letter-spacing:2px;color:#333}

/* announcement */
.announce{top:774px;height:228px;background:var(--teal);color:var(--white)}
.announce h2{position:absolute;left:150px;top:58px;font-family:'Cinzel',serif;font-weight:400;font-size:38px}
.announce p{position:absolute;left:150px;top:114px;width:620px;font-weight:700;font-size:18px;line-height:24px}
.outline{border:2px solid var(--white)}

/* about */
.about{top:1002px;height:609px}
.about-mark{left:265px;top:110px;width:205px;height:420px;display:flex;align-items:center;justify-content:center;text-align:center;font-family:'Cinzel',serif;font-size:40px;line-height:1.25;color:var(--teal)}
.about h2{position:absolute;left:535px;top:145px;font-family:'Cinzel',serif;font-weight:500;font-size:44px;color:var(--teal)}
.about p{position:absolute;left:535px;top:212px;width:490px;font-size:15px;line-height:25.6px;color:#333}

/* service band */
.times{top:1611px;height:349px;background:linear-gradient(120deg,#6f8196 0%,#a9b6c4 45%,#c6ced6 70%,#8f7158 88%,#6f5844 100%)}
.notch{left:570px;top:0}
.band-col{top:108px;color:var(--white)}
.band-col h3{font-family:'Cinzel',serif;font-weight:400;font-size:26px;display:flex;align-items:center;gap:12px;margin-bottom:14px}
.band-col table{border-collapse:collapse;font-weight:700;font-size:17px}
.band-col td{height:33px}
.band-col td.c{padding:0 20px 0 24px}
.band-col p{font-size:17px;line-height:21px;padding-left:0}

/* pastor */
.pastor{top:1960px;height:599px;background:var(--teal)}
.pastor-photo{left:0;top:0}
.size-note{left:195px;top:280px;font-size:26px;color:#9aa39a}
.pastor h2{position:absolute;left:640px;width:440px;top:70px;text-align:center;font-family:'Cinzel',serif;font-weight:500;font-size:46px;color:var(--white)}
.pastor p.bio{position:absolute;left:640px;width:440px;top:140px;text-align:center;font-size:15.5px;line-height:25.5px;color:var(--white)}
.pastor blockquote{position:absolute;left:640px;width:440px;top:395px;text-align:center;font-style:italic;font-weight:700;font-size:20px;line-height:31px;color:var(--white)}

/* articles */
.faith{top:2559px;height:1246px}
.faith h2{position:absolute;left:0;width:1200px;top:88px;text-align:center;font-family:'Cinzel',serif;font-weight:500;font-size:44px;color:var(--teal)}
.timeline-line{left:598px;top:200px;width:3px;height:932px;background:var(--teal)}
.node{position:absolute;width:54px;height:54px;border-radius:50%;background:var(--white);border:3px solid #b7c8b0;box-shadow:inset 0 -6px 10px rgba(0,0,0,.12)}
.node.strong{border-color:#3c5a3a}
.belief{position:absolute;width:320px;font-size:13px;line-height:19.5px;color:#555}
.belief h4{font-weight:900;font-size:17px;color:#111;margin-bottom:6px}
.belief.left{left:208px;text-align:right}
.belief.right{left:678px;text-align:left}
.belief .quote{font-weight:700;color:#222;margin-bottom:14px}
.belief ul{list-style:none;margin-top:24px}

/* support */
.support{top:3805px;height:314px;background:var(--green-dark);color:var(--white);text-align:center}
.support h2{position:absolute;left:0;width:1200px;top:70px;font-family:'Cinzel',serif;font-weight:500;font-size:48px}
.support p{position:absolute;left:270px;width:660px;top:137px;font-size:17px;line-height:25px}

/* contact */
.contact{top:4119px;height:488px;background:#85a96b}
.contact h2{position:absolute;left:150px;top:70px;font-family:'Cinzel',serif;font-weight:500;font-size:50px;color:var(--white)}
.contact p{position:absolute;left:150px;top:135px;width:400px;font-size:17px;line-height:24px;color:var(--white)}
.field{position:absolute;background:var(--white);border:1px solid #dcdcdc;font-size:11px;color:#888;padding:6px 8px}

/* footer */
.footer{top:4607px;height:504px;background:var(--teal);color:var(--white)}
.footer-brand{left:110px;top:150px;width:240px;text-align:center;font-family:'Cinzel',serif;font-size:28px;line-height:1.2}
.social{top:325px;width:22px;height:22px;border-radius:50%;background:var(--white)}
.divider{top:95px;width:3px;height:230px;background:var(--white)}
.footer h5{font-family:'Cinzel',serif;font-weight:400;font-size:19px;position:absolute}
.footer .info{position:absolute;font-size:13px;line-height:16px}
.footer ul{position:absolute;list-style:none;font-size:13px}
.footer li{height:41px}
.legal{left:136px;top:453px;font-size:11px}
.foot-btn{left:897px;top:434px;width:168px;height:46px;background:var(--green-deep);border:2px solid var(--white);font-size:15px}
</style>
</head>
<body>

<!-- HERO -->
<section class="section hero" role="img" aria-label="Photo of the brick church building under an overcast sky">
  <div class="abs hours">
    <h3><svg width="18" height="18" viewBox="0 0 18 18"><rect x="1" y="3" width="16" height="14" rx="2" fill="none" stroke="#333" stroke-width="2"/><rect x="1" y="3" width="16" height="4" fill="#333"/><rect x="4" y="0" width="2" height="5" fill="#333"/><rect x="12" y="0" width="2" height="5" fill="#333"/></svg>Service Times</h3>
    <table>
      <tr><td>Wednesday Evening Service</td><td class="c">:</td><td>7:30 PM</td></tr>
      <tr><td>Sunday School</td><td class="c">:</td><td>10:00 AM</td></tr>
      <tr><td>Sunday Morning Service</td><td class="c">:</td><td>11:00 AM</td></tr>
      <tr><td>Sunday Evening Service</td><td class="c">:</td><td>5:30 PM</td></tr>
    </table>
  </div>

  <div class="abs brand">Grace Covenant<br>Church</div>

  <a class="pill top-btn" style="left:794px;width:118px;background:var(--green-dark)">DONATE</a>
  <a class="pill top-btn" style="left:918px;width:132px;background:var(--green)">LISTEN LIVE</a>
  <a class="pill top-btn" style="left:1058px;width:96px;background:var(--teal)">LOGIN</a>

  <nav class="abs nav">
    <a class="active">HOME</a>
    <a>SUPPORT US</a>
    <a>RECORDING LIBRARY</a>
  </nav>

  <h1 class="abs headline">WE LOVE BECAUSE<br>HE FIRST LOVED US</h1>
</section>

<!-- ANNOUNCEMENT -->
<section class="section announce">
  <h2>ANNOUNCEMENT TEXT</h2>
  <p>Lorem ipsum dolor sit amet, con sectetur adipiscing elit, sed do eiusmod tempor incididet, con sectetur adi...</p>
  <a class="pill outline" style="left:882px;top:86px;width:164px;height:52px;font-size:18px">READ MORE</a>
</section>

<!-- ABOUT -->
<section class="section about">
  <div class="abs about-mark">Grace<br>Covenant<br>Church</div>
  <h2>About Our Church</h2>
  <p>Lorem ipsum dololor sit amet, consectetur ladip iscing elit, sed do eiusmod tempor incididunlt ut labore et dolore magna aliqua. oreu is ipousum suspendisse ultrices gravida. Risus comlomodo viverra maecenas accumslacus vel facilisis. Lorem ipsum dololor sit amet, consectetur ladip iscing elit, sed do eiusmod tempor incididu nlt ut labore et dolore magna aliqua. Qloreuis ipousum suspendisse ultr ices gravida. Risus comlomodo viverra maecenas accumslacus vel facilisis. Lorem ipsum dololor sit amet, consectetur ladip iscing elit, sed do eiusmod tempor incididunlt .</p>
  <a class="pill" style="left:538px;top:473px;width:146px;height:43px;background:var(--green)">READ MORE</a>
</section>

<!-- SERVICE TIMES / ADDRESS -->
<section class="section times" role="img" aria-label="Photo of a wooden cross against a cloudy sky">
  <svg class="abs notch" width="60" height="26" viewBox="0 0 60 26"><polygon points="0,0 60,0 30,26" fill="#fff"/></svg>
  <div class="abs band-col" style="left:150px">
    <h3><svg width="20" height="20" viewBox="0 0 18 18"><rect x="1" y="3" width="16" height="14" rx="2" fill="none" stroke="#fff" stroke-width="2"/><rect x="1" y="3" width="16" height="4" fill="#fff"/><rect x="4" y="0" width="2" height="5" fill="#fff"/><rect x="12" y="0" width="2" height="5" fill="#fff"/></svg>Service Times</h3>
    <table>
      <tr><td>Wednesday Evening Service</td><td class="c">:</td><td>7:30 PM</td></tr>
      <tr><td>Sunday School</td><td class="c">:</td><td>10:00 AM</td></tr>
      <tr><td>Sunday Morning Service</td><td class="c">:</td><td>11:00 AM</td></tr>
      <tr><td>Sunday Evening Service</td><td class="c">:</td><td>5:30 PM</td></tr>
    </table>
  </div>
  <div class="abs band-col" style="left:594px">
    <h3><svg width="16" height="22" viewBox="0 0 16 22"><path d="M8 0C3.6 0 0 3.6 0 8c0 6 8 14 8 14s8-8 8-14c0-4.4-3.6-8-8-8z" fill="#fff"/><circle cx="8" cy="8" r="3" fill="#8fa0b2"/></svg>Address</h3>
    <p>Location name Dummy<br>Street name 243<br>Lorem 7987 Dummy</p>
  </div>
</section>

<!-- PASTOR -->
<section class="section pastor">
  <svg class="abs pastor-photo" width="1200" height="599" viewBox="0 0 1200 599" role="img" aria-label="Portrait photo of the pastor">
    <polygon points="0,0 625,0 565,599 0,599" fill="#7fa866"/>
    <polygon points="0,0 595,0 505,599 0,599" fill="#4e7232"/>
  </svg>
  <div class="abs size-note">1000X1000</div>
  <h2>PASTOR</h2>
  <p class="bio">Lorem ipsum dololor sit amet, consectetur ladip iscing elit, sed do eiusmod tempor incididunlt ut labore et dolore magna aliqua. oreu is ipousum suspendisse ultrices gravida. Risus comlomodo viverra maecenas accumslacus vel facilisis. Lorem ipsum dololor sit amet, consectetur ladip iscing elit, sed do eiusmod tempor incididu nlt ut</p>
  <a class="pill" style="left:794px;top:322px;width:142px;height:40px;background:var(--green-dark);font-size:13px">OUR STREAMHALL</a>
  <blockquote>“And I will give you pastors according to mine heart, which shall feed you with knowledge and understanding. Jer 3:15 KJV”</blockquote>
</section>

<!-- ARTICLES OF FAITH -->
<section class="section faith">
  <h2>ARTICLES OF FAITH</h2>
  <div class="abs timeline-line"></div>
  <div class="node" style="left:572px;top:203px"></div>
  <div class="node strong" style="left:572px;top:307px"></div>
  <div class="node" style="left:572px;top:506px"></div>
  <div class="node strong" style="left:572px;top:688px"></div>
  <div class="node" style="left:572px;top:813px"></div>
  <div class="node strong" style="left:572px;top:933px"></div>
  <div class="node" style="left:572px;top:1033px"></div>

  <div class="belief left" style="top:200px">
    <h4>THE GOD HEAD.</h4>
    We believe in the God head bodily, known as the Divine Trinity. This body consist of God the father, Jesus Christ, his only begotten son and the redeemer of the world, and of the Holy Ghost, The third
  </div>

  <div class="belief right" style="top:330px;width:365px">
    <h4>FULL SALVATION.</h4>
    We believe that Salvation is received only when a person comes to the realization that he or she is lost and separated from God and becomes full of godly sorrow, confessing their sins and true repentance, believing in the shed blood of the Lord Jesus Christ as the only sacrifice for sins. Through the blood of Christ we have:
    <ul>
      <li>(1) remission of sins, Matthew 26:28 Heb 9:22</li>
      <li>(2) Sanctification. Hebrews 13:12</li>
      <li>(3) redemption. Revelations 5:9</li>
      <li>(4) cleansing. 1 John 1:7 Rev. 1:5</li>
      <li>(5). Justification. Romans 5:9</li>
    </ul>
  </div>

  <div class="belief left" style="top:516px">
    <h4>SANCTIFICATION.</h4>
    <div class="quote">“Sanctify them through thy truth thy word is truth St John 17:17. For this is the will of God even your sanctification”</div>
    We believe in a set apart life, separate from the world to Christ 2 Cor 6:17-18
  </div>

  <div class="belief right" style="top:703px;width:360px">
    <h4>BAPTISM OF THE HOLY GHOST.</h4>
    We believe in the baptism of the Holy Ghost as it is taught in the Bible and promised by our Lord Jesus Christ, with peaking in tongues as the Spirit gives utterance as the initial evidence. Acts 2:4 we believe that the gift of the Holy Ghost is for all believers as the Lord promised. Acts 2:17-18
  </div>

  <div class="belief left" style="top:821px;left:212px">
    <h4>DIVINE HEALING.</h4>
    We believe Divine Healing to be included in the atonement of Jesus Christ our Lord, And believe that it is still for us today. 1 Peter 2:24 Luke 9:1-2 Mark 16-18 James 5:15
  </div>

  <div class="belief right" style="top:942px">
    <h4>SECOND COMING OF CHRIST.</h4>
    We believe in the second coming of Jesus Christ. Matthew 24:44 Luke 12:40
  </div>

  <div class="belief left" style="top:1022px;left:208px">
    <h4>ETERNITY.</h4>
    We believe in Literal Eternity. Eternal Life for the believer and eternal death for those without Christ. Revelations 21:1-27
  </div>
</section>

<!-- SUPPORT -->
<section class="section support">
  <h2>Support Us</h2>
  <p>Lorem ipsum dololor sit amet, consectetur ladip iscing elit, sed do eiusmod temp utorem ipsum dololor sit amet, consectetur ladip iscing od temput et.</p>
  <a class="pill" style="left:510px;top:205px;width:182px;height:42px;background:var(--green)">DONATE NOW</a>
</section>

<!-- CONTACT -->
<section class="section contact">
  <svg class="abs" style="left:0;top:0" width="1200" height="488" viewBox="0 0 1200 488">
    <polygon points="700,0 740,0 600,488 560,488" fill="#4e7232"/>
    <polygon points="740,0 1200,0 1200,488 600,488" fill="#b08c6a" role="img" aria-label="Photo of the brick church building and parking lot"/>
  </svg>
  <h2>Contact Us</h2>
  <p>Lorem ipsum dololor sit amet, consectetur ladip iscing elit, sed do eiusmod temput labore et.</p>
  <div class="field" style="left:153px;top:213px;width:192px;height:34px">Name</div>
  <div class="field" style="left:355px;top:213px;width:191px;height:34px">Email</div>
  <div class="field" style="left:153px;top:271px;width:393px;height:108px">Message</div>
  <a class="pill" style="left:150px;top:401px;width:110px;height:40px;background:var(--green-dark);font-size:14px">SUBMIT</a>
</section>

<!-- FOOTER -->
<footer class="section footer">
  <div class="abs footer-brand">Grace Covenant<br>Church</div>
  <div class="abs social" style="left:186px"></div>
  <div class="abs social" style="left:219px"></div>
  <div class="abs social" style="left:252px"></div>

  <div class="abs divider" style="left:361px"></div>
  <div class="abs divider" style="left:654px"></div>
  <div class="abs divider" style="left:871px"></div>

  <h5 style="left:393px;top:95px">MAILING ADDRESS:</h5>
  <svg class="abs" style="left:396px;top:143px" width="14" height="20" viewBox="0 0 16 22"><path d="M8 0C3.6 0 0 3.6 0 8c0 6 8 14 8 14s8-8 8-14c0-4.4-3.6-8-8-8z" fill="#fff"/><circle cx="8" cy="8" r="3" fill="#00b4d4"/></svg>
  <div class="info" style="left:423px;top:142px">PO Box 1816000,<br>Dummy Locat, 0092178-900</div>

  <h5 style="left:393px;top:217px">CONTACT:</h5>
  <svg class="abs" style="left:396px;top:268px" width="18" height="18" viewBox="0 0 24 24"><path d="M6.6 10.8a15 15 0 006.6 6.6l2.2-2.2c.3-.3.7-.4 1-.2 1.1.4 2.3.6 3.6.6.6 0 1 .4 1 1V20c0 .6-.4 1-1 1C10.6 21 3 13.4 3 4c0-.6.4-1 1-1h3.5c.6 0 1 .4 1 1 0 1.3.2 2.5.6 3.6.1.3 0 .7-.2 1L6.6 10.8z" fill="#fff"/></svg>
  <div class="info" style="left:423px;top:265px">Phone:<br>8998 XXX X XX</div>
  <svg class="abs" style="left:395px;top:318px" width="20" height="14" viewBox="0 0 20 14"><rect width="20" height="14" rx="1" fill="#fff"/><path d="M1 1l9 7 9-7" fill="none" stroke="#00b4d4" stroke-width="1.5"/></svg>
  <div class="info" style="left:423px;top:313px">Email:<br>info@gracecovenantchurch.org</div>

  <h5 style="left:694px;top:95px">RESOURCES</h5>
  <ul style="left:694px;top:142px">
    <li>ResourcesTestimonials</li>
    <li>Wakening Grace</li>
    <li>Sermons</li>
    <li>Articles of faith</li>
    <li>Contact us</li>
  </ul>

  <h5 style="left:903px;top:95px">LINKS</h5>
  <ul style="left:903px;top:142px">
    <li>Events</li>
    <li>Christian Education</li>
    <li>Membership &amp; Outreach</li>
    <li>Music</li>
    <li>Stewardship</li>
  </ul>

  <div class="abs legal">GraceCovenantChurch @2023 All Rights are reserved.Privacy Policy and Terms of Service apply.</div>
  <a class="pill foot-btn">Donate Now</a>
</footer>

</body>
</html>
```